Stationery Design For Specialist London law firm

We have merged two firms of London lawyers to create a new firm with a new name.

The new firms name is KR Holloway. We would like to include the description Solicitors and Advocates in the design.

We need a new design for our headed paper, business cards compliment slips etc.

The image we wish to project is fresh but not gimmicky - reliable and strong but not stuffy.

We have no strong views on font or colour this really is pretty much a blank page.

Our preference is for the name to be at the top of the page

Target Market(s)

Our clients who are individuals rather than corporate and other lawyers

Industry/Entity Type

Law Firm

Requirements
Should not have
• Legal images eg scales of justice etc

Obviously nothing childish or gimmicky

```html
<!DOCTYPE html>
<html lang="en">
<head>
<meta charset="utf-8">
<title>KR Holloway — Stationery</title>
<link href="https://fonts.googleapis.com/css2?family=Arimo:wght@400;700&family=Roboto+Condensed:wght@300;400&display=swap" rel="stylesheet">
<style>
  :root {
    --teal: #1f6a62;
    --teal-deep: #175a55;
    --lime: #bad636;
    --ink: #1a1a1a;
    --grey-text: #6d6d6d;
    --paper: #ffffff;
    --backdrop: #d3d3d3;
    --backdrop-mark: #c2c2c2;
    --band: linear-gradient(90deg, var(--teal) 0%, #4f9360 45%, var(--lime) 100%);
  }
  * { box-sizing: border-box; margin: 0; padding: 0; }
  html, body { width: 1200px; height: 900px; overflow: hidden; }
  body {
    background: var(--backdrop);
    font-family: "Arimo", Arial, sans-serif;
    color: var(--ink);
    position: relative;
  }

  /* backdrop brand mark */
  .backdrop-mark {
    position: absolute; left: 38px; top: 40px;
    display: flex; flex-direction: column; align-items: flex-start; gap: 10px;
    color: var(--backdrop-mark);
  }
  .backdrop-mark .square { width: 150px; height: 150px; background: var(--backdrop-mark); }
  .backdrop-mark .name { font-size: 22px; letter-spacing: 6px; font-weight: 400; }

  /* shared */
  .sheet { position: absolute; background: var(--paper); overflow: hidden; }
  .band { position: absolute; left: 0; right: 0; background: var(--band); }
  .brand { display: flex; align-items: center; gap: 5px; color: var(--teal); font-weight: 700; white-space: nowrap; }
  .brand .square { background: var(--teal); flex: none; }
  .divider { position: absolute; width: 1px; background: #9a9a9a; }
  .tagline { font-family: "Roboto Condensed", Arial, sans-serif; font-weight: 300; color: var(--teal); line-height: 1.25; }

  /* letterhead */
  .letterhead { left: 584px; top: 78px; width: 514px; height: 726px; }
  .letterhead .band-top { top: 0; height: 8px; }
  .letterhead .band-bottom { bottom: 0; height: 21px; }
  .letterhead .brand { position: absolute; left: 30px; top: 130px; font-size: 11px; }
  .letterhead .brand .square { width: 12px; height: 12px; }
  .letterhead .tagline { position: absolute; left: 88px; top: 52px; font-size: 8.5px; letter-spacing: 0.6px; }
  .letterhead .divider { left: 82px; top: 46px; height: 60px; }
  .letterhead .logo-block { position: absolute; left: 30px; top: 52px; width: 50px; }
  .letterhead .logo-block .brand { position: static; flex-direction: column; align-items: flex-start; gap: 4px; font-size: 8px; }
  .letterhead .logo-block .square { width: 40px; height: 40px; }
  .contact-block {
    position: absolute; text-align: right; color: var(--grey-text);
    font-size: 5.6px; line-height: 1.3;
  }
  .contact-block .firm { color: var(--teal); font-weight: 700; }
  .contact-block .gap { height: 5px; }
  .letterhead .contact-block { right: 35px; top: 50px; }
  .letter-body { position: absolute; left: 56px; top: 182px; width: 428px; font-size: 7.4px; line-height: 11px; }
  .letter-body .subject { font-weight: 700; font-size: 8.4px; margin-bottom: 40px; }
  .letter-body p { text-align: justify; margin-bottom: 11px; }
  .letter-body .sign-off { margin-top: 48px; }
  .letter-body .sign-off strong { display: block; }

  /* business card front */
  .card-front { left: 260px; top: 238px; width: 284px; height: 164px; }
  .card-front .band-top { top: 0; height: 6px; }
  .card-front .logo-block { position: absolute; left: 22px; top: 96px; }
  .card-front .logo-block .brand { flex-direction: column; align-items: flex-start; gap: 3px; font-size: 6px; }
  .card-front .logo-block .square { width: 30px; height: 30px; }
  .card-front .divider { left: 66px; top: 72px; height: 74px; }
  .card-details { position: absolute; left: 74px; top: 70px; font-size: 7.6px; line-height: 9.4px; color: var(--grey-text); }
  .card-details .person { color: var(--teal); }
  .card-details .address { margin-top: 12px; }
  .card-details .tel { margin-top: 12px; }

  /* business card back */
  .card-back {
    left: 440px; top: 322px; width: 280px; height: 164px;
    background: linear-gradient(100deg, var(--teal-deep) 20%, #5e9b5a 60%, var(--lime) 100%);
    color: #fff; text-align: center;
  }
  .card-back .brand { position: absolute; left: 0; right: 0; top: 42px; flex-direction: column; gap: 6px; color: #fff; font-size: 11px; }
  .card-back .brand .square { width: 46px; height: 46px; background: #fff; }
  .card-back .tagline { position: absolute; left: 0; right: 0; top: 112px; color: #fff; font-size: 10px; letter-spacing: 1.6px; }

  /* compliment slip */
  .comp-slip { left: 79px; top: 529px; width: 461px; height: 215px; }
  .comp-slip .band-top { top: 0; height: 8px; }
  .comp-slip .band-bottom { bottom: 0; height: 15px; }
  .comp-slip .greeting {
    position: absolute; left: 29px; top: 89px;
    font-family: "Roboto Condensed", Arial, sans-serif; font-weight: 400;
    font-size: 19px; color: var(--teal);
  }
  .comp-slip .logo-block { position: absolute; left: 29px; top: 122px; }
  .comp-slip .logo-block .brand { flex-direction: column; align-items: flex-start; gap: 4px; font-size: 7px; }
  .comp-slip .logo-block .square { width: 38px; height: 38px; }
  .comp-slip .divider { left: 78px; top: 122px; height: 58px; }
  .comp-slip .tagline { position: absolute; left: 84px; top: 124px; font-size: 8px; letter-spacing: 0.5px; }
  .comp-slip .contact-block { right: 218px; top: 133px; font-size: 5px; }
</style>
</head>
<body>

  <div class="backdrop-mark" aria-hidden="true">
    <div class="square"></div>
    <div class="name">KR HOLLOWAY</div>
  </div>

  <!-- headed paper -->
  <section class="sheet letterhead" aria-label="Headed paper">
    <div class="band band-top"></div>
    <div class="logo-block">
      <div class="brand"><span class="square"></span><span>KR Holloway</span></div>
    </div>
    <div class="divider"></div>
    <div class="tagline">Solicitors And<br>Advocates</div>
    <div class="contact-block">
      <div class="firm">KR Holloway</div>
      <div>Company Address</div>
      <div>And Contact Information</div>
      <div>Company Address And</div>
      <div>Contact Information</div>
      <div class="gap"></div>
      <div>Contact Information Contact Information</div>
      <div>Contact Information Contact</div>
    </div>

    <div class="letter-body">
      <div class="subject">Lorem ipsum dolor sit amet, consectetur adipiscing elit</div>
      <p>Lorem ipsum dolor sit amet, consectetur adipiscing elit. Nam lobortis pellentesque ligula nec volutpat. Pellentesque eget metus dapibus consequat non sed leo. Class aptent taciti sociosqu ad litora torquent per conubia nostra, per inceptos himenaeos. Proin adipiscing dignissim enim eget congue. Vivamus eu commodo mauris ac quam malesuada at venenatis orci tincidunt. Mauris tincidunt varius condimentum mi eget laoreet. Aliquam semper tortor at libero porta at lacinia luctus enim ut leo lobortis condimentum ac sed sapien.</p>
      <p>Nulla lobortis ante, vel tempus sapien fringilla nec. Sed eget lectus dictum diam imperdiet neque eu quam dapibus lobortis. Morbi vestibulum turpis sed urna lacinia volutpat. Donec condimentum, diam ut tempor iaculis, odio enim viverra nisi, nec rutrum. Vestibulum ante ipsum primis in faucibus orci luctus et ultrices posuere cubilia non mauris feugiat molestie a vel mauris. Vestibulum enim elit, ultrices a ultrices libero. Donec fringilla, lorem tempor condimentum convallis, libero dolor condimentum imperdiet neque arcu at nisi. Morbi tempor metus quis lectus mattis at lacinia orci pretium. Quisque nunc vitae lorem sollicitudin ut molestie justo interdum. Sed vestibulum tellus neque. Donec laoreet faucibus nulla, eu tempor turpis rhoncus non. Aenean mattis volutpat tortor urna, ullamcorper sed vestibulum vel, ultricies ut neque.</p>
      <p>Cras eu orci at nunc aliquam accumsan. Maecenas tempus tristique felis, id consequat diam vestibulum at. Suspendisse dapibus ipsum in justo rutrum iaculis. Sed sed augue vel diam ullamcorper tincidunt. Nulla facilisi. Aliquam quis auctor lorem. Nullam magna velit, interdum in auctor id, venenatis et nunc. Nullam vel metus id leo vulputate placerat in eu dolor. In scelerisque, erat eget faucibus fermentum, nisl sem venenatis mi, in blandit quam magna in nunc. Morbi id ligula quis purus lacinia elementum et quis ligula. Curabitur risus odio, eleifend eget consectetur sed, convallis a libero. Suspendisse posuere rhoncus ipsum blandit imperdiet. Ut congue, tellus quis lobortis accumsan, nisi sapien lobortis justo, a convallis ipsum enim id eros. Sed nec lectus id turpis consequat vestibulum tristique et felis. Lorem ipsum dolor sit amet, consectetur adipiscing elit. Donec scelerisque metus eu dolor faucibus ut auctor sapien ullamcorper.</p>
      <div class="sign-off">
        <strong>Lorem ipsum dolor,</strong>
        <div>Consectetur Adipiscing</div>
        <div>Sapien Ullamcorper</div>
      </div>
    </div>
    <div class="band band-bottom"></div>
  </section>

  <!-- business card, front -->
  <section class="sheet card-front" aria-label="Business card front">
    <div class="band band-top"></div>
    <div class="logo-block">
      <div class="brand"><span class="square"></span><span>KR Holloway</span></div>
    </div>
    <div class="divider"></div>
    <div class="card-details">
      <div class="person">Name Surname</div>
      <div>Advocate</div>
      <div class="address">Address Address,<br>Address Address 44 - 44<br>Address</div>
      <div class="tel">Tel. no. 444 444 444</div>
    </div>
  </section>

  <!-- business card, back -->
  <section class="sheet card-back" aria-label="Business card back">
    <div class="brand"><span class="square"></span><span>KR Holloway</span></div>
    <div class="tagline">Solicitors And Advocates</div>
  </section>

  <!-- compliment slip -->
  <section class="sheet comp-slip" aria-label="Compliment slip">
    <div class="band band-top"></div>
    <div class="greeting">With Compliments</div>
    <div class="logo-block">
      <div class="brand"><span class="square"></span><span>KR Holloway</span></div>
    </div>
    <div class="divider"></div>
    <div class="tagline">Solicitors And<br>Advocates</div>
    <div class="contact-block">
      <div class="firm">KR Holloway</div>
      <div>Company Address</div>
      <div>And Contact Information</div>
      <div>Company Address And</div>
      <div>Contact Information</div>
      <div class="gap"></div>
      <div>Contact Information Contact Information</div>
      <div>Contact Information Contact</div>
    </div>
    <div class="band band-bottom"></div>
  </section>

</body>
</html>
```